Speech Pathology card for parents of young children

I need a professional, yet fun card for my speech and language pathology services.
I'm trying to offer my speech therapy services to parents of young children. These parents will most likely be women. I want the card to have a fun feel to it and have a concept of speech and language in it (kind of like the cartoon I've attached below showing a boy/girl talking).

I'd want a white background on the card and to bring in some bright colors as well.

Please include the NOVRE logo in a smaller size on a free corner of the card.

Target Market(s)

parents of young children

Contact Information for Business Card

must have my information and I'd like it to have the NOVRE logo (small) somewhere in the corner)

Font styles to use
Serif
Sans Serif

Colors

Designer to choose colors to be used in the design.

Requirements
Must have
• The card title should read: Speech-Language Pathologist
• Lorena Tuvell
• MS CCC-SLP/TSSLD (this under the name)
• 555 014 2786
• lorentuvell@quillpost.net
Nice to have
• i'm looking for a card with a white background and a fun icon that encompasses speaking... similar to the one I've attached.

```html
<!DOCTYPE html>
<html lang="en">
<head>
<meta charset="utf-8">
<title>Lorena Tuvell – Business Card</title>
<link rel="stylesheet" href="https://fonts.googleapis.com/css2?family=Roboto:wght@300;400;500;700&display=swap">
<style>
  :root {
    --backdrop: #e9e6e1;
    --card: #ffffff;
    --teal: #12bcd6;
    --orange: #f5ab2c;
    --ink: #4a4a4a;
    --ink-soft: #6d6d6d;
    --pink: #ec4f9a;
    --art-a: #eef0f2;
    --art-b: #dfe6ea;
  }
  * { margin: 0; padding: 0; box-sizing: border-box; }
  html, body {
    width: 1200px; height: 1023px; overflow: hidden;
    background: var(--backdrop);
    font-family: "Roboto", Arial, sans-serif;
  }
  .card {
    position: absolute; left: 75px; top: 211px;
    width: 1050px; height: 600px;
    background: var(--card);
    overflow: hidden;
    box-shadow: 0 14px 40px rgba(0,0,0,.18);
  }
  .card__wave { position: absolute; inset: 0; width: 1050px; height: 600px; }
  .identity {
    position: absolute; right: 52px; top: 160px; text-align: right;
  }
  .identity__name {
    font-size: 58px; font-weight: 500; color: var(--orange); letter-spacing: .5px; line-height: 68px;
  }
  .identity__credentials {
    font-size: 30px; font-weight: 400; color: var(--ink); letter-spacing: .5px; line-height: 38px;
  }
  .identity__title {
    font-size: 22px; font-weight: 300; color: var(--ink-soft); letter-spacing: .5px; line-height: 32px;
  }
  .card__rule {
    position: absolute; left: 390px; right: 52px; top: 314px;
    height: 2px; background: var(--orange);
  }
  .association {
    position: absolute; right: 52px; top: 336px;
    display: flex; align-items: center; gap: 14px;
  }
  .association__dot {
    width: 54px; height: 54px; border-radius: 50%; background: #1d1d1d;
  }
  .association__name {
    font-size: 26px; font-weight: 400; color: var(--ink); letter-spacing: 3px;
  }
  .speech-art {
    position: absolute; left: 60px; top: 390px; width: 200px; height: 160px;
    border-radius: 6px;
    background: linear-gradient(135deg, var(--art-a), var(--art-b));
  }
  .website {
    position: absolute; left: 272px; top: 382px;
    font-size: 20px; font-weight: 700; color: var(--pink);
  }
  .contact {
    position: absolute; left: 390px; top: 466px; list-style: none;
  }
  .contact__item {
    display: flex; align-items: center; gap: 14px;
    font-size: 30px; font-weight: 300; color: var(--ink-soft); line-height: 46px;
  }
  .contact__icon { width: 18px; height: 18px; flex: none; }
</style>
</head>
<body>
  <div class="card">
    <svg class="card__wave" viewBox="0 0 1050 600" aria-hidden="true">
      <path d="M0,0 H1050 V38 C860,52 660,110 460,196 C300,262 140,300 0,312 Z" fill="var(--teal)"/>
      <path d="M0,330 C150,318 320,276 480,210 C680,128 870,66 1050,52 V62 C880,80 690,142 490,226 C330,292 160,338 0,352 Z" fill="var(--orange)"/>
    </svg>

    <div class="identity">
      <div class="identity__name">Lorena Tuvell</div>
      <div class="identity__credentials">MS CCC-SLP/TSSLD</div>
      <div class="identity__title">Speech-Language Pathologist</div>
    </div>

    <div class="card__rule"></div>

    <div class="association">
      <span class="association__dot"></span>
      <span class="association__name">NOVRE</span>
    </div>

    <div class="speech-art" role="img" aria-label="Hand-drawn cartoon of a child shouting through a megaphone"></div>
    <div class="website">talkbloom.com</div>

    <ul class="contact">
      <li class="contact__item">
        <svg class="contact__icon" viewBox="0 0 18 18" aria-hidden="true"><path d="M4 1 L7 5 L5 7 C6 10 8 12 11 13 L13 11 L17 14 L15 17 C8 17 1 10 1 3 Z" fill="var(--orange)"/></svg>
        555 014 2786
      </li>
      <li class="contact__item">
        <svg class="contact__icon" viewBox="0 0 18 18" aria-hidden="true"><rect x="1.5" y="3.5" width="15" height="11" fill="none" stroke="var(--orange)" stroke-width="2"/><path d="M2 4 L9 10 L16 4" fill="none" stroke="var(--orange)" stroke-width="2"/></svg>
        lorentuvell@quillpost.net
      </li>
    </ul>
  </div>
</body>
</html>
```